Pharma compliance business needs an eye catching academic poster

Academic poster for display at a pharma industry conference

Background

ClinoVerse Ltd is an online, on-demand supplier of compliance advice (copy review) to the life science industry. See www.clinoverse-demo.co.uk for more info.

We have conducted a benchmarking study on the time spent by three large pharma companies on copy review. It highlights time spent and time wasted as a result of unnecessary, additional rounds of review. As a result we have developed recommendation for improving the copy review process.

Requirement

We need an academic poster A0 Landscape (841 x 1189 mm) that summaries our methodology, results and conclusions. We have written the copy - see attached.

This poster will be displayed at the QTE 8th Annual Continental Health Knowledge and Outreach Summit - See more at: http://www.qtehub-example.org/Events-and-Courses/Find-Events-and-Courses/Event-Details.aspx?ProductID=7481536&EventType=Meeting#sthash.kW4pQx2n.dpuf.

Audience

Attendees of this conference are budget holders and decision makers. They can chose to outsource copy review to organisation like ours, however, many pharma companies currently keep this function is house and waste internal resource, time and money.

Objective

Our objective is demonstrate from our findings that massive savings can be found by getting copy right first time.

Design Guidelines

This poster should not be heavily branded - as this CANNOT be promotional however you may include our logo with the authors names. We would like you to use our brand guidelines, however, in order that it is clear that this study was conducted by ourselves. Brand book is attached plus our logos and icons.

Examples of academic posters can be found with a quick google search - one source that I have found useful is http://brendalowicke-example.com/tips/academic/posterdesign I have attached an example of the kind of layout we would like to see... please keep the background quite plain as this will make it easier to read

Within the copy attached data graphs have been included for position guidance only and an excel file with the raw data and graphs is also attached - if you feel that the data can be displayed more effectively please do... also please apply our brand style. It is important that the data is accurately reproduced.

```html
<!DOCTYPE html>
<html lang="en">
<head>
<meta charset="utf-8">
<title>Copy Review Resource Utilisation – Academic Poster</title>
<link rel="stylesheet" href="https://fonts.googleapis.com/css2?family=Arimo:wght@400;700&display=swap">
<style>
:root{
  --slate:#5b7299;
  --slate-dark:#4a5f85;
  --frame:#8b9dc4;
  --frame-light:#c3cce3;
  --ink:#2c2d70;
  --title:#6e84aa;
  --bg:#eceef7;
  --panel:#ffffff;
  --blue:#4a7ac9;
  --red:#d0494a;
  --green:#9ccf4e;
}
*{box-sizing:border-box;margin:0;padding:0}
html,body{width:1200px;height:848px;overflow:hidden;background:var(--bg)}
body{font-family:"Arimo",Arial,sans-serif;color:var(--ink)}
.poster{position:relative;width:1200px;height:848px;overflow:hidden;background:var(--bg)}
.backdrop{position:absolute;inset:0;
  background:radial-gradient(circle at 20% 30%,#f6f7fc 0,transparent 18%),
  radial-gradient(circle at 70% 15%,#f4f5fb 0,transparent 14%),
  radial-gradient(circle at 85% 75%,#f3f4fb 0,transparent 20%),
  radial-gradient(circle at 40% 80%,#f4f5fb 0,transparent 16%),
  linear-gradient(180deg,#eef0f8,#e6e9f4)}
.abs{position:absolute}
.brand{left:58px;top:30px;display:flex;align-items:center;gap:8px;
  font-size:24px;font-weight:700;color:var(--slate)}
.brand .dot{width:18px;height:18px;border-radius:50%;background:var(--slate)}
.title{left:200px;top:18px;width:990px;text-align:center;font-size:17.5px;font-weight:700;
  letter-spacing:2.4px;line-height:24px;color:var(--title);text-transform:uppercase}
.authors{left:200px;top:80px;width:990px;text-align:center;font-size:14px;font-weight:700;
  letter-spacing:1px;color:var(--slate)}
.authors .sep{display:inline-block;width:9px;height:9px;border-radius:50%;background:var(--slate);margin:0 14px;vertical-align:1px}
.frame{left:22px;top:112px;width:1158px;height:728px;border:2px solid var(--frame);border-radius:14px}
.frame-inner{left:30px;top:120px;width:1142px;height:712px;border:1px solid var(--frame-light);border-radius:10px}
.panel{position:absolute;background:var(--panel);border:3px solid var(--frame);border-radius:16px;
  box-shadow:0 0 0 4px #fff,0 0 0 5px var(--frame-light);overflow:hidden}
.tab{position:absolute;background:var(--slate);color:#fff;font-weight:700;font-size:14px;
  letter-spacing:1.5px;height:28px;line-height:28px;padding:0 18px;
  border:2px solid #fff;box-shadow:0 0 0 1px var(--slate);
  clip-path:polygon(0 0,calc(100% - 10px) 0,100% 50%,calc(100% - 10px) 100%,0 100%)}
.tab.center{clip-path:polygon(10px 0,calc(100% - 10px) 0,100% 50%,calc(100% - 10px) 100%,10px 100%,0 50%)}
.body-text{font-size:7.4px;line-height:11px;color:var(--ink)}
.body-text p{margin-bottom:8px}
.indent{text-indent:14px}
.ticks{list-style:none;margin:-3px 0 8px 10px}
.ticks li{display:flex;gap:5px;align-items:flex-start}
.ticks svg{flex:none;width:10px;height:10px;margin-top:0}
.chart{position:absolute;background:#fff;border:1px solid #cfd4e4;box-shadow:1px 1px 3px rgba(60,70,110,.25)}
.chart svg{display:block;width:100%;height:100%}
.rule{left:612px;top:195px;width:1px;height:620px;background:var(--frame-light)}
.ranked{position:absolute;left:620px;top:410px;width:262px;border-collapse:collapse;font-size:7.4px;text-align:center;background:#fff}
.ranked td,.ranked th{border:1px solid #9aa3b8;height:25px;font-weight:400;color:#222}
.ranked caption{border:1px solid #9aa3b8;border-bottom:0;font-size:9px;padding:3px;background:#fff;color:#222}
.ranked thead th{height:14px}
.callout{position:absolute;background:var(--slate);color:#fff;text-align:center;font-size:7.4px;line-height:10.5px;font-weight:700}
.step{position:absolute;top:694px;width:70px;height:110px;background:var(--slate-dark);color:#fff;
  font-size:6.8px;line-height:9.6px;text-align:center;padding:22px 5px 5px;
  clip-path:polygon(0 12%,50% 0,100% 12%,100% 100%,0 100%)}
.brand-tile{left:982px;top:692px;width:136px;height:84px;background:linear-gradient(160deg,#7b8fb3,#5b7299);
  display:flex;align-items:center;justify-content:center;gap:7px;color:#fff;font-size:19px;font-weight:700;border:2px solid #fff}
.brand-tile .dot{width:13px;height:13px;border-radius:50%;background:#fff}
</style>
</head>
<body>
<svg width="0" height="0" style="position:absolute">
  <defs>
    <symbol id="tick" viewBox="0 0 10 10">
      <circle cx="5" cy="5" r="4.3" fill="none" stroke="#5b7299" stroke-width="1"/>
      <path d="M2.8 5.2l1.5 1.5 3-3.2" fill="none" stroke="#5b7299" stroke-width="1.1"/>
    </symbol>
  </defs>
</svg>
<div class="poster">
  <div class="backdrop" role="img" aria-label="Soft pale lavender background of overlapping faint circles"></div>

  <div class="abs brand"><span class="dot"></span>ClinoVerse</div>
  <h1 class="abs title">A survey of three pharmaceutical companies’ resource utilisation in copy<br>review activities and proposals for business process improvement.</h1>
  <div class="abs authors">Mara Linden, director, ClinoVerse Ltd, London<span class="sep"></span>Owen Falk, director, ClinoVerse Ltd, London</div>

  <div class="abs frame"></div>
  <div class="abs frame-inner"></div>

  <section class="panel intro" style="left:45px;top:140px;width:230px;height:455px">
    <div class="body-text" style="padding:38px 14px 0 14px">
      <p class="indent">Promotional and non-promotional materials are highly visible outputs of pharmaceutical companies. They are scrutinised by competitors, agencies and sometimes customers. Penalties for errors can be significant, measured in time, reputation or monetary fines.</p>
      <p class="indent">Central to nearly all codes and systems are requirements that statements and messages are:</p>
      <ul class="ticks">
        <li><svg><use href="#tick"/></svg>Consistent with the marketing authorisation</li>
        <li><svg><use href="#tick"/></svg>Accurate and capable of substantiation</li>
        <li><svg><use href="#tick"/></svg>Fair, balanced and up to date</li>
      </ul>
      <p>Regional and national differences exist in the regulation of:</p>
      <ul class="ticks">
        <li><svg><use href="#tick"/></svg>Meetings</li>
        <li><svg><use href="#tick"/></svg>Gifts, fees, hospitality and travel</li>
        <li><svg><use href="#tick"/></svg>External approval requirements</li>
        <li><svg><use href="#tick"/></svg>Dispute resolution</li>
      </ul>
      <p class="indent">The UK industry body, NPIA, issued a code of conduct in 1958. Its current form is very similar to the European industry ERPA code. Many UK pharmaceutical companies place considerable importance on adherence to the code, with large teams working on the review of materials and activities.</p>
      <p class="indent">Copy review is now a significant activity that consumes considerable resources, in the form of time, of some of the most expensive and scientifically able members of staff.</p>
      <div style="display:flex;gap:6px;margin-top:10px">
        <svg width="13" height="13" viewBox="0 0 13 13" style="flex:none"><circle cx="6.5" cy="6.5" r="5.8" fill="none" stroke="#5b7299"/><path d="M6.5 3.5v6M3.5 6.5h6" stroke="#5b7299" stroke-width="1.2"/></svg>
        <p style="margin:0">The aims of this study were to:<br>quantify time taken up by copy review activities in a sample of UK pharmaceutical affiliates medical results.</p>
      </div>
    </div>
  </section>
  <div class="tab" style="left:40px;top:148px;width:148px">INTRODUCTION</div>

  <section class="panel method" style="left:45px;top:625px;width:230px;height:203px">
    <div class="body-text" style="padding:40px 12px 0 12px">
      <p>We developed an online survey with three components:</p>
      <ul class="ticks" style="margin-left:0">
        <li><svg><use href="#tick"/></svg>Retrospective, quantitative estimates of time taken on copy review and numbers of avoidable iterations</li>
        <li><svg><use href="#tick"/></svg>Ranking the common reasons for avoidable iterations</li>
        <li><svg><use href="#tick"/></svg>Free text responses describing potential solutions</li>
      </ul>
      <p>This was sent to 249 staff in three UK pharmaceutical companies in 2013 and 2014.</p>
    </div>
  </section>
  <div class="tab" style="left:40px;top:633px;width:110px">METHOD</div>

  <section class="panel results" style="left:285px;top:140px;width:630px;height:690px"></section>
  <div class="tab center" style="left:540px;top:150px;width:120px;text-align:center">RESULTS</div>
  <div class="abs rule"></div>

  <div class="abs body-text" style="left:310px;top:194px;width:285px">
    <p class="indent">We received 118 usable responses from 249 invitations, a response rate of 47%. 48 responses were from medical affairs and 70 from commercial and other functions.</p>
    <p class="indent">The proportion of the working week spent on copy review by physicians was a consistent 40%. For medical information, the proportion varied between zero and 65%. Scientific advisors spent 0% to 42% of their time on copy activities.</p>
  </div>

  <div class="chart" style="left:298px;top:298px;width:92px;height:58px">
    <svg viewBox="0 0 92 58"><line x1="8" y1="48" x2="60" y2="48" stroke="#aaa" stroke-width=".5"/>
      <rect x="14" y="12" width="6" height="36" fill="var(--blue)"/><rect x="30" y="24" width="6" height="24" fill="var(--blue)"/><rect x="46" y="8" width="6" height="40" fill="var(--blue)"/>
      <text x="63" y="24" font-size="3.5" fill="#555">Physicians</text></svg>
  </div>
  <div class="chart" style="left:396px;top:298px;width:92px;height:58px">
    <svg viewBox="0 0 92 58"><line x1="8" y1="48" x2="60" y2="48" stroke="#aaa" stroke-width=".5"/>
      <rect x="14" y="20" width="6" height="28" fill="var(--red)"/><rect x="30" y="10" width="6" height="38" fill="var(--red)"/><rect x="46" y="30" width="6" height="18" fill="var(--red)"/>
      <text x="63" y="24" font-size="3.5" fill="#555">Medical info</text></svg>
  </div>
  <div class="chart" style="left:494px;top:298px;width:92px;height:58px">
    <svg viewBox="0 0 92 58"><line x1="8" y1="48" x2="60" y2="48" stroke="#aaa" stroke-width=".5"/>
      <rect x="14" y="26" width="6" height="22" fill="var(--green)"/><rect x="30" y="14" width="6" height="34" fill="var(--green)"/><rect x="46" y="34" width="6" height="14" fill="var(--green)"/>
      <text x="63" y="24" font-size="3.5" fill="#555">Scientists</text></svg>
  </div>

  <div class="abs body-text" style="left:310px;top:368px;width:285px">
    <p class="indent">On average just over 50% of time spent on copy activities went on checking scientific statements and claims. The remainder was spent on concept and planning meetings, commissioning, proof reading, compiling materials. Rounds of scheduled review averaged 2.3.</p>
  </div>

  <div class="chart" style="left:310px;top:424px;width:162px;height:112px">
    <svg viewBox="0 0 162 112">
      <text x="81" y="11" font-size="7" font-weight="700" text-anchor="middle" fill="#222">% of copy time x activity, all MA %</text>
      <g transform="translate(12,17) scale(.76)">
        <path d="M60 60 L60 10 A50 50 0 1 1 44.5 107.6Z" fill="#6f9fe0"/>
        <path d="M60 60 L44.5 107.6 A50 50 0 0 1 19.5 30.6Z" fill="#e06a6a"/>
        <path d="M60 60 L19.5 30.6 A50 50 0 0 1 38.7 14.8Z" fill="#b7dc78"/>
        <path d="M60 60 L38.7 14.8 A50 50 0 0 1 60 10Z" fill="#a58ccc"/>
      </g>
      <g font-size="3.6" fill="#444">
        <rect x="108" y="46" width="3" height="3" fill="#6f9fe0"/><text x="113" y="49">Statements and claims</text>
        <rect x="108" y="53" width="3" height="3" fill="#e06a6a"/><text x="113" y="56">Meetings</text>
        <rect x="108" y="60" width="3" height="3" fill="#b7dc78"/><text x="113" y="63">Compiling</text>
        <rect x="108" y="67" width="3" height="3" fill="#a58ccc"/><text x="113" y="70">Commissioning</text>
      </g>
    </svg>
  </div>

  <div class="abs body-text" style="left:484px;top:446px;width:110px">
    <p>Estimates of the proportion of jobs requiring avoidable rounds of review ranged between 30 and 50%.</p>
  </div>

  <div class="chart" style="left:414px;top:546px;width:126px;height:98px">
    <svg viewBox="0 0 126 98">
      <text x="63" y="11" font-size="7" font-weight="700" text-anchor="middle" fill="#222">% jobs needing extra rounds %</text>
      <g stroke="#e3e3e3" stroke-width=".4"><line x1="12" y1="22" x2="90" y2="22"/><line x1="12" y1="38" x2="90" y2="38"/><line x1="12" y1="54" x2="90" y2="54"/><line x1="12" y1="70" x2="90" y2="70"/><line x1="12" y1="84" x2="90" y2="84"/></g>
      <rect x="20" y="28" width="12" height="56" fill="var(--blue)"/>
      <rect x="45" y="42" width="12" height="42" fill="var(--blue)"/>
      <rect x="70" y="50" width="12" height="34" fill="var(--blue)"/>
      <g font-size="4" fill="#444"><text x="24" y="91">A</text><text x="49" y="91">B</text><text x="74" y="91">C</text></g>
      <rect x="93" y="40" width="3" height="3" fill="var(--blue)"/><text x="98" y="43" font-size="3.4" fill="#444">% jobs extra</text>
    </svg>
  </div>

  <div class="abs body-text" style="left:310px;top:598px;width:100px">
    <p>This results in between six and eight additional hours work per week ...</p>
  </div>

  <div class="chart" style="left:300px;top:668px;width:115px;height:150px">
    <svg viewBox="0 0 115 150">
      <text x="57" y="14" font-size="7" font-weight="700" text-anchor="middle" fill="#222">Phys</text>
      <g stroke="#e3e3e3" stroke-width=".4"><line x1="12" y1="30" x2="80" y2="30"/><line x1="12" y1="60" x2="80" y2="60"/><line x1="12" y1="90" x2="80" y2="90"/><line x1="12" y1="120" x2="80" y2="120"/></g>
      <rect x="20" y="58" width="11" height="62" fill="var(--blue)"/>
      <rect x="40" y="42" width="11" height="78" fill="var(--blue)"/>
      <rect x="60" y="66" width="11" height="54" fill="var(--blue)"/>
      <text x="46" y="136" font-size="4" fill="#444" text-anchor="middle">Company</text>
      <rect x="84" y="68" width="3" height="3" fill="var(--blue)"/><text x="89" y="71" font-size="3.6" fill="#444">Hours</text>
    </svg>
  </div>
  <div class="chart" style="left:452px;top:668px;width:123px;height:150px">
    <svg viewBox="0 0 123 150">
      <text x="61" y="14" font-size="7" font-weight="700" text-anchor="middle" fill="#222">SA/MSL</text>
      <g stroke="#e3e3e3" stroke-width=".4"><line x1="12" y1="30" x2="86" y2="30"/><line x1="12" y1="60" x2="86" y2="60"/><line x1="12" y1="90" x2="86" y2="90"/><line x1="12" y1="120" x2="86" y2="120"/></g>
      <rect x="22" y="46" width="12" height="74" fill="var(--green)"/>
      <rect x="44" y="56" width="12" height="64" fill="var(--green)"/>
      <rect x="66" y="86" width="12" height="34" fill="var(--green)"/>
      <text x="50" y="136" font-size="4" fill="#444" text-anchor="middle">Company</text>
      <rect x="90" y="68" width="3" height="3" fill="var(--green)"/><text x="95" y="71" font-size="3.6" fill="#444">Hours</text>
    </svg>
  </div>

  <div class="chart" style="left:620px;top:215px;width:112px;height:86px">
    <svg viewBox="0 0 112 86">
      <text x="48" y="11" font-size="6.5" font-weight="700" text-anchor="middle" fill="#222">Friction</text>
      <rect x="20" y="38" width="9" height="38" fill="#6f9fe0"/><rect x="44" y="26" width="9" height="50" fill="#6f9fe0"/><rect x="68" y="34" width="9" height="42" fill="#6f9fe0"/>
      <line x1="12" y1="76" x2="86" y2="76" stroke="#aaa" stroke-width=".5"/>
      <rect x="90" y="40" width="3" height="3" fill="#6f9fe0"/><text x="95" y="43" font-size="3.4" fill="#444">Friction</text>
    </svg>
  </div>
  <div class="chart" style="left:745px;top:190px;width:96px;height:72px">
    <svg viewBox="0 0 96 72">
      <text x="44" y="11" font-size="6.5" font-weight="700" text-anchor="middle" fill="#222">Med info</text>
      <rect x="34" y="32" width="8" height="30" fill="#e06a6a"/><rect x="54" y="26" width="8" height="36" fill="#e06a6a"/>
      <line x1="12" y1="62" x2="76" y2="62" stroke="#aaa" stroke-width=".5"/>
      <text x="44" y="69" font-size="3.4" fill="#444" text-anchor="middle">Company</text>
    </svg>
  </div>
  <div class="chart" style="left:735px;top:270px;width:100px;height:76px">
    <svg viewBox="0 0 100 76">
      <text x="46" y="11" font-size="6.5" font-weight="700" text-anchor="middle" fill="#222">Missed deadlines</text>
      <rect x="18" y="40" width="8" height="26" fill="var(--green)"/><rect x="40" y="22" width="8" height="44" fill="var(--green)"/><rect x="62" y="34" width="8" height="32" fill="var(--green)"/>
      <line x1="12" y1="66" x2="78" y2="66" stroke="#aaa" stroke-width=".5"/>
      <rect x="80" y="30" width="3" height="3" fill="var(--green)"/><text x="84" y="33" font-size="3" fill="#444">Missed</text>
    </svg>
  </div>

  <div class="abs body-text" style="left:625px;top:360px;width:262px">
    <p>... and raised levels of friction, reported as ‘frequent’ or ‘common’ by 80% in one organization and to a significant level in all three.</p>
  </div>

  <table class="ranked">
    <caption>Ranked reasons for re-work</caption>
    <thead><tr><th>A</th><th>B</th><th>C</th><th></th></tr></thead>
    <tbody>
      <tr><td>1</td><td>3</td><td>2</td><td>Claims<br>not supportable</td></tr>
      <tr><td>2</td><td>1</td><td>1</td><td>References missing<br>or not marked</td></tr>
      <tr><td>3</td><td>4</td><td>4</td><td>Difference in opinion<br>in interpreting the Code</td></tr>
      <tr><td>6</td><td>3</td><td>3</td><td>Spelling and<br>grammar</td></tr>
      <tr><td>4</td><td>5</td><td>5</td><td>Other technical<br>Code issue</td></tr>
      <tr><td>5</td><td>7</td><td>6</td><td>Review criteria<br>changed during project</td></tr>
      <tr><td>7</td><td>6</td><td>7</td><td>Layout or<br>presentation</td></tr>
    </tbody>
  </table>

  <div class="abs body-text" style="left:625px;top:622px;width:262px">
    <p>... and raised levels of friction, reported as ‘frequent’ or ‘common’ by 80% in one organization and to a significant level in all three.</p>
  </div>

  <div class="callout" style="left:640px;top:646px;width:222px;height:40px;padding:4px 8px">Free text proposed solutions from respondents were grouped subjectively into themes. The three most frequently cited proposals were:</div>
  <div class="step" style="left:640px">Meetings to discuss materials before copy got into the review cycle.</div>
  <div class="step" style="left:716px">Improve the scientific accuracy and spelling of copy before review, so that it is right first time.</div>
  <div class="step" style="left:792px">Insist on consistency between reviewers and between reviews cycles.</div>

  <section class="panel conclusion" style="left:922px;top:140px;width:228px;height:690px">
    <div class="body-text" style="padding:46px 12px 0 14px">
      <p class="indent">Between one third and one half of the available resource in medical affairs teams in the UK is taken up reviewing materials. This varies between organisations depending upon allocation of this activity. Materials are seen multiple times and a significant proportion of iterations are seen again and again. This causes loss of productivity and internal friction between and within departments. Scientists and physicians engaged in review have positive proposals for process improvement, which are consistent across the organisations involved in this piece of work.</p>
      <p class="indent">This small survey identifies potential best practice. The interventions proposed are not proven to reduce waste in the copy review process. However, it seems likely that pharmaceutical companies could save time and money by adopting some simple solutions aimed at ensuring only good quality, scientifically valid material enters the review cycle, and by defining review standards, roles and responsibilities. Physicians and scientists could be released from desk work to undertake customer facing activities or conduct studies. Hard to fill posts and subsequent reliance on contractors could be reduced.</p>
      <p class="indent">This activity has crept up on the industry, to the point now that reviewing copy has become an industry within an industry, occupying half of the working lives of hundreds of medical information specialists and pharmaceutical physicians in the UK. This is not mission critical work and is a diversion from the productive and real work of supporting patients and helping customers to understand medicines.</p>
      <p class="indent">An industry-wide prospective survey is necessary to identify actual resource utilisation in this activity and benchmark best vs worst practice. Process improvement interventions could be formally assessed to measure the savings that can be made.</p>
      <p class="indent" style="margin-bottom:4px">It is likely that three relatively simple actions could save a lot of time:</p>
      <ul class="ticks" style="margin-top:0">
        <li><svg><use href="#tick"/></svg>Improve the standards of materials entering the review cycle</li>
        <li><svg><use href="#tick"/></svg>Define and limit responsibilities</li>
      </ul>
    </div>
  </section>
  <div class="tab" style="left:945px;top:148px;width:160px;text-align:center">CONCLUSION</div>

  <div class="abs brand-tile"><span class="dot"></span>ClinoVerse</div>
</div>
</body>
</html>
```